Coffee bag and coffee beer revamp

We need a coffee bag design where we can print two stickers and they fit nicely on the bag. this is an example of 500gr bag. We will also need 250gr and 1kilo versions.

One the logo attached and the other the coffee description details attached.
This should sit nicely on the white bag example attached.
One is also a photo of what we have but it needed some work to make sure dimensions are good and its clear.
Example: attached of text and these will be variable values that we need the label to edit and they should be different colour labels - we have 6 types of coffee.

<COFFEE TYPE> example House BLEND
<DATE ROASTED> 17/03/23
Text always the same -- "Consume within 12 months"

I have also attache the font and original files. There can be some colour added.

Other types of coffee

SIDAMO
GUATEMALA
SANTOS
COSTA RICA
SUPREMO
DECAF

The beer is just the logo and text "Bendula Cold Brew Coffee" label with the date and logo.

Target Market(s)

coffee lovers

Industry/Entity Type

food

Font styles to use
Other font styles liked:
• i will upload the fonts

Colors
EB3D1F
EC4F4E
F09395
F8D3D4
FCEDEE

Requirements
Nice to have
• can try alternative colour? even just for labels

```html
<!DOCTYPE html>
<html lang="en">
<head>
<meta charset="utf-8">
<title>Bendula Coffee – Sidamo 250g</title>
<link rel="stylesheet" href="https://fonts.googleapis.com/css2?family=Montserrat:wght@600;700;800&family=Roboto+Slab:wght@700;800&display=swap">
<style>
  :root {
    --backdrop: #1f1415;
    --bag-white: #f7f7f8;
    --bag-shade: #e9e9ec;
    --roast-brown: #4b2c2e;
    --roast-brown-soft: #6e4b4d;
    --label-text: #ffffff;
  }
  * { margin: 0; padding: 0; box-sizing: border-box; }
  html, body {
    width: 1200px;
    height: 1114px;
    overflow: hidden;
    background: var(--backdrop);
  }
  .canvas {
    position: relative;
    width: 1200px;
    height: 1114px;
  }
  .bag-face {
    position: absolute;
    left: 300px;
    top: 97px;
    width: 600px;
    height: 920px;
    background: linear-gradient(180deg, var(--bag-white) 0%, #ffffff 45%, var(--bag-shade) 100%);
    border-radius: 14px 14px 6px 6px;
  }
  .top-seal {
    position: absolute;
    top: 34px;
    left: 50%;
    transform: translateX(-50%);
    width: 54px;
    height: 54px;
    border-radius: 50%;
    background: var(--roast-brown);
    color: var(--label-text);
    font: 800 12px "Roboto Slab", serif;
    display: flex;
    align-items: center;
    justify-content: center;
    letter-spacing: 0.5px;
  }
  .zip-line {
    position: absolute;
    left: 0;
    right: 0;
    top: 118px;
    height: 6px;
    border-top: 1px solid #d8d8dc;
    border-bottom: 1px solid #e4e4e8;
  }
  .brand-badge {
    position: absolute;
    left: 180px;
    top: 263px;
    width: 240px;
    text-align: center;
    color: var(--roast-brown);
  }
  .badge-artwork {
    width: 190px;
    height: 250px;
    margin: 0 auto;
    border-radius: 95px 95px 12px 12px;
    background: linear-gradient(180deg, var(--roast-brown-soft) 0%, var(--roast-brown) 100%);
  }
  .brand-name {
    margin-top: 14px;
    font: 800 40px/1 "Roboto Slab", serif;
    letter-spacing: 2px;
  }
  .brand-sub {
    margin-top: 4px;
    font: 700 11px "Roboto Slab", serif;
    letter-spacing: 4px;
  }
  .arabica {
    margin-top: 12px;
    font: 800 17px "Roboto Slab", serif;
    letter-spacing: 2px;
  }
  .roast-date-line {
    margin-top: 6px;
    font: 700 11px "Montserrat", sans-serif;
    letter-spacing: 0.5px;
    white-space: nowrap;
  }
  .variety-label {
    position: absolute;
    left: 178px;
    top: 704px;
    width: 242px;
    height: 91px;
    border-radius: 10px;
    background: var(--roast-brown);
    text-align: center;
    padding-top: 14px;
  }
  .variety-name {
    color: var(--label-text);
    font: 700 24px/1 "Montserrat", sans-serif;
    letter-spacing: 0.5px;
  }
  .net-weight {
    display: inline-block;
    margin-top: 12px;
    width: 214px;
    padding: 5px 0;
    border-radius: 6px;
    background: var(--label-text);
    color: var(--roast-brown);
    font: 700 12px "Montserrat", sans-serif;
  }
  .net-weight small { font-size: 9px; }
  .brew-guide {
    position: absolute;
    left: 67px;
    top: 838px;
  }
  .roast-level {
    display: flex;
    gap: 5px;
    margin-top: 10px;
  }
  .roast-dot {
    width: 9px;
    height: 9px;
    border-radius: 50%;
    border: 1.5px solid var(--roast-brown);
  }
  .roast-dot.is-filled { background: var(--roast-brown); }
</style>
</head>
<body>
<main class="canvas">
  <section class="bag-face">
    <div class="top-seal">Bendula</div>
    <div class="zip-line"></div>

    <div class="brand-badge">
      <div class="badge-artwork" role="img" aria-label="Vintage engraved illustration of a woman holding a coffee cup inside an arched badge"></div>
      <div class="brand-name">BENDULA</div>
      <div class="brand-sub">COFFEE</div>
      <div class="arabica">100% ARABICA</div>
      <div class="roast-date-line">GEBRAND OP / TORREFIE LE / ROASTED ON</div>
    </div>

    <div class="variety-label">
      <div class="variety-name">SIDAMO</div>
      <div class="net-weight">250g <small>(Net Wt. 8.8 Oz)</small> NETTO</div>
    </div>

    <div class="brew-guide">
      <svg class="brew-icons" width="102" height="22" viewBox="0 0 102 22" fill="none" stroke="#4b2c2e" stroke-width="1.5" aria-label="Suitable brewing methods">
        <path d="M2 6h12l-2 14H4z"/><path d="M4 3h8"/>
        <rect x="20" y="4" width="12" height="16" rx="1"/><path d="M26 1v3M22 9h8"/>
        <path d="M38 6l8 8M44 4l6 6M48 16h4"/>
        <path d="M56 12h14M60 12v-6h6v6M58 16h10v4H58z"/>
        <path d="M80 2h10l-2 8h4l-2 10h-10l-2-10h4z"/>
      </svg>
      <div class="roast-level" aria-label="Roast level 4 of 6">
        <span class="roast-dot is-filled"></span>
        <span class="roast-dot is-filled"></span>
        <span class="roast-dot is-filled"></span>
        <span class="roast-dot is-filled"></span>
        <span class="roast-dot"></span>
        <span class="roast-dot"></span>
      </div>
    </div>
  </section>
</main>
</body>
</html>
```